Keenfield Athletics Powerpoint Template

We need a Powerpoint Template design for a new company based in Ottawa (Canada), called Keenfield Athletics. We help team sport coaches and sport programs improve their teams and develop their athletes better.

Basically, I would like to have a professionnal, beautiful, and minimalist powerpoint template that I could then used to support the workshops, courses, and keynote presentations I give.

Attached is a file that contains all the information necessary for our logos, colors, and fonts. I would have to be able to present the "template" either as Keenfield Athletics (Corporate ID) or as Coach Dorian (personal brand).

Thank you for your interest,

Target Market(s)

Athletic Directors of Universities, High-Performance Team Sport Coaches

Industry/Entity Type

It Company

Font styles to use
Sans Serif

Requirements
Must have
• These are all template slides that I would like to have designed (I will fill them with the content for each presentation): (a) Title slide, (b) Heading and text slide, (c) 2 large images with subtitles, (d) 3 large images with subtitles, (e) large image with text, (f) large image with subtitle, (g) quote slide, and (h) 3 key points
Nice to have
• Personalized to Coach Dorian and Keenfield Athletics, but not mandatory. The emphasis should NOT be put on the brand, but rather on the ability for viewers to see the text and understand the message.

```html
<!DOCTYPE html>
<html lang="en">
<head>
<meta charset="utf-8">
<title>Keenfield Athletics – Presentation Template</title>
<link href="https://fonts.googleapis.com/css2?family=Montserrat:wght@500;600;700&family=Open+Sans:wght@400;600;700&display=swap" rel="stylesheet">
<style>
  :root{
    --navy-bg:#0c2640;
    --blue:#2f62bd;
    --orange:#e8571f;
    --ink:#2a3550;
    --text:#2b2b2b;
    --white:#ffffff;
    --grey-box:#555a60;
    --photo-night:linear-gradient(180deg,#1c2533 0%,#33404f 45%,#2e3d22 75%,#3c4d25 100%);
    --photo-action:linear-gradient(135deg,#22378a 0%,#3a5bc4 40%,#c9d1e6 60%,#1f3390 100%);
  }
  *{margin:0;padding:0;box-sizing:border-box}
  html,body{width:1200px;height:1200px;overflow:hidden;background:var(--navy-bg)}
  body{position:relative;font-family:"Open Sans",Arial,sans-serif;color:var(--text)}
  .slide{position:absolute;width:464px;height:262px;background:var(--white);overflow:hidden}
  .photo{position:absolute}
  .photo--night{background:var(--photo-night)}
  .photo--action{background:var(--photo-action)}
  .abs{position:absolute}
  .h-mont{font-family:"Montserrat",Arial,sans-serif}
  .wordmark{font-family:"Montserrat",Arial,sans-serif;font-weight:700;color:var(--ink);text-transform:uppercase;line-height:1;text-align:center}
  .stripe-blue{position:absolute;background:var(--blue)}
  .stripe-orange{position:absolute;background:var(--orange)}
  .lorem{font-size:7px;line-height:10.4px}

  /* title */
  .title-slide{left:69px;top:34px;width:463px;height:261px}
  .title-slide .photo{inset:0;background:linear-gradient(120deg,#dfe3ec 0%,#eef0f4 40%,#e3e6ee 70%,#d9dde8 100%)}
  .title-brand{position:absolute;left:0;right:0;top:92px;display:flex;align-items:center;justify-content:center;gap:12px}
  .title-brand .mark{width:22px;height:22px;background:var(--ink)}
  .title-brand .wordmark{font-size:34px;text-align:left}
  .title-brand .wordmark span{display:block;font-size:34px;margin-top:4px}

  /* team */
  .team-slide{left:646px;top:28px;width:481px;height:271px}
  .team-slide .photo{left:0;top:0;width:481px;height:136px}
  .team-title{position:absolute;top:34px;width:100%;text-align:center;color:var(--white);font-size:19px;font-family:"Open Sans",sans-serif}
  .portrait{position:absolute;top:85px;width:100px;height:97px;clip-path:polygon(0 0,100% 0,100% 80%,50% 100%,0 80%);background:linear-gradient(180deg,#e8e8e8,#b9bcc0)}
  .member{position:absolute;top:191px;width:110px;font-size:6.5px;text-align:center}
  .member em{display:block;font-size:4.6px}
  .member ul{text-align:left;margin-top:6px;padding-left:14px;font-size:4.8px;line-height:7px}
  .brand-tab{position:absolute;left:0;bottom:0;width:45px;height:37px;background:var(--white);box-shadow:0 0 4px rgba(0,0,0,.25);display:flex;align-items:center;justify-content:center}
  .brand-tab .wordmark{font-size:5.5px}

  /* heading + text */
  .text-slide{left:68px;top:330px}
  .text-art{left:0;top:0;z-index:0}
  .text-title{left:236px;top:34px;color:var(--blue);font-size:12.5px;font-weight:600;white-space:nowrap;z-index:1}
  .text-body{left:263px;top:75px;width:186px;z-index:1}

  /* quote */
  .quote-slide{left:654px;top:330px}
  .badge{position:absolute;border-radius:50%;background:var(--white);display:flex;align-items:center;justify-content:center}
  .badge .wordmark{font-size:6px}
  .quote-label{left:85px;top:172px;color:var(--blue);font-weight:700;font-size:12px}
  .quote-marks{left:33px;top:186px;color:var(--blue);font-family:Georgia,serif;font-size:80px;line-height:1;font-weight:700}
  .quote-text{left:86px;top:206px;width:300px;font-size:6.4px;line-height:9.4px;color:#444}

  /* orange panel */
  .panel-slide{left:67px;top:622px;width:465px}
  .panel-side{position:absolute;left:0;top:0;width:198px;height:262px;background:var(--orange);color:var(--white)}
  .panel-heading{left:7px;top:6px;font-size:28px;line-height:28px;font-weight:700}
  .panel-item h3{font-size:7.4px;font-weight:400;text-transform:uppercase}
  .panel-item p{font-size:5.3px;line-height:7.8px;margin-top:3px;width:140px}

  /* grid */
  .grid-slide{left:654px;top:622px}
  .grid-title{top:2px;width:100%;text-align:center;color:var(--blue);font-size:22px;font-weight:600}
  .grid-box{position:absolute;color:var(--white);padding:16px 10px 0}
  .grid-box h3{font-size:9.5px;font-weight:400;text-transform:uppercase;margin-bottom:8px}
  .grid-row{display:flex;gap:6px;align-items:flex-start;font-size:6.4px;line-height:9px;margin-bottom:9px}
  .grid-row svg{flex:none;margin-top:2px}
  .grid-box--right{text-align:right}

  /* benefits */
  .benefit-slide{left:68px;top:914px}
  .benefit-title{left:249px;top:16px;width:200px;font-size:16px;line-height:20px;font-weight:600;color:var(--ink)}
  .benefit-sub{left:249px;top:59px;font-size:9.5px}
  .benefit{position:absolute;left:246px;display:flex;gap:9px}
  .tick{width:28px;height:28px;flex:none;display:flex;align-items:center;justify-content:center}
  .benefit h4{font-size:5.6px;font-weight:700;margin-top:3px}
  .benefit p{font-size:4.4px;line-height:6.6px;color:#555;margin-top:2px}

  /* stats */
  .stats-slide{left:654px;top:914px}
  .stats-title{left:37px;top:14px;font-size:16px;font-weight:600;color:var(--ink)}
  .stats-sub{left:37px;top:35px;font-size:9px}
  .stats-box{position:absolute;left:218px;top:62px;width:214px;height:131px;background:var(--blue);padding:10px 0 0 20px;color:var(--white)}
  .stats-box p{border-left:1.5px solid var(--white);padding-left:8px;font-size:5.2px;line-height:6.6px;margin-bottom:14px;height:20px;display:flex;align-items:center}
  .stats-foot{left:37px;top:203px;font-size:7.2px}
</style>
</head>
<body>

<!-- Title slide -->
<section class="slide title-slide">
  <div class="photo" role="img" aria-label="Faded photo of football players in blue uniforms"></div>
  <div class="title-brand">
    <div class="mark"></div>
    <div class="wordmark">Keenfield<span>Athletics</span></div>
  </div>
</section>

<!-- Management team -->
<section class="slide team-slide">
  <div class="photo photo--night" role="img" aria-label="Football linemen crouched at night under stadium lights"></div>
  <div class="team-title">Management Team</div>
  <div class="portrait" style="left:82px" role="img" aria-label="Portrait of team member"></div>
  <div class="portrait" style="left:190px;background:linear-gradient(180deg,#3b6b3a,#8bb2d8)" role="img" aria-label="Portrait of team member"></div>
  <div class="portrait" style="left:299px" role="img" aria-label="Portrait of team member"></div>
  <div class="member" style="left:78px">John Doe<em>Managing Director</em>
    <ul><li>Lorem ipsum dolor sit amet, consectetuer a</li><li>Lorem ipsum dolor sit amet, consectetuer a</li></ul></div>
  <div class="member" style="left:186px">Michelle Harlow<em>Sports Director</em>
    <ul><li>Lorem ipsum dolor sit amet, consectetuer a</li><li>Lorem ipsum dolor sit amet, consectetuer a</li></ul></div>
  <div class="member" style="left:294px">Jane Doe<em>Trainee</em>
    <ul><li>Lorem ipsum dolor sit amet, consectetuer a</li><li>Lorem ipsum dolor sit amet, consectetuer a</li></ul></div>
  <div class="stripe-blue" style="left:45px;top:258px;width:436px;height:5px"></div>
  <div class="stripe-orange" style="left:45px;top:263px;width:436px;height:6px"></div>
  <div class="brand-tab"><div class="wordmark">Keenfield<br>Athletics</div></div>
</section>

<!-- Heading and text -->
<section class="slide text-slide">
  <svg class="abs text-art" width="464" height="262" viewBox="0 0 464 262">
    <defs><linearGradient id="runnerTone" x1="0" y1="0" x2="1" y2="1"><stop offset="0" stop-color="#c9d2dc"/><stop offset=".5" stop-color="#8a8f96"/><stop offset="1" stop-color="#5d6066"/></linearGradient></defs>
    <path d="M170 0 C236 50 240 190 178 262 L166 262 C224 190 220 60 156 0Z" fill="var(--blue)"/>
    <path d="M0 0 H146 C206 60 210 190 154 262 H0Z" fill="url(#runnerTone)" role="img" aria-label="Athlete tying his running shoe on a city street"/>
    <path d="M196 66 C210 130 200 210 162 262 L152 262 C190 210 198 130 188 74Z" fill="var(--orange)"/>
  </svg>
  <div class="abs text-title h-mont">LOREM IPSUM DOLOR SIT AMET,</div>
  <p class="abs text-body lorem">Lorem ipsum dolor sit amet, consectetuer adipiscing elit. Aenean commodo ligula eget dolor. Aenean massa. Cum sociis natoque penatibus et magnis dis parturient montes, nascetur ridiculus mus. Donec quam felis, ultricies nec, pellentesque eu, pretium quis, sem. Nulla consequat massa quis enim. Donec pede justo, fringilla vel, aliquet nec, vulputate eget, arcu. In enim justo, rhoncus ut, imperdiet a, venenatis vitae, justo. Nullam dictum</p>
  <div class="stripe-blue" style="left:190px;top:249px;width:274px;height:5px"></div>
  <div class="stripe-orange" style="left:180px;top:254px;width:284px;height:8px"></div>
</section>

<!-- Quote -->
<section class="slide quote-slide">
  <svg class="abs" width="464" height="262" viewBox="0 0 464 262">
    <defs><linearGradient id="nightTone" x1="0" y1="0" x2="0" y2="1"><stop offset="0" stop-color="#1c2533"/><stop offset=".5" stop-color="#34404f"/><stop offset="1" stop-color="#3b4c25"/></linearGradient></defs>
    <path d="M0 0 H464 V130 C440 200 380 210 300 190 C250 178 220 168 190 166 C120 150 60 110 0 80Z" fill="url(#nightTone)" role="img" aria-label="Football linemen in blue helmets crouched on a field at night"/>
    <path d="M464 130 C440 200 380 210 300 190 C250 178 220 168 190 166" fill="none" stroke="var(--blue)" stroke-width="2"/>
    <circle cx="156" cy="126" r="38" fill="none" stroke="#9aa3b4" stroke-width="2" stroke-dasharray="10 4"/>
    <path d="M156 88 A38 38 0 0 1 194 126" fill="none" stroke="var(--blue)" stroke-width="3"/>
  </svg>
  <div class="badge" style="left:124px;top:94px;width:64px;height:64px"><div class="wordmark">Keenfield<br>Athletics</div></div>
  <div class="abs quote-label h-mont">QUOTE</div>
  <div class="abs quote-marks">”</div>
  <p class="abs quote-text">Lorem ipsum dolor sit amet, consectetuer adipiscing elit. Aenean commodo ligula eget dolor. Aenean massa. Cum sociis natoque penatibus et magnis dis parturient montes, nascetur ridiculus mus. Donec quam felis, ultricies nec, pellentesque eu, pretium quis, sem. Nulla consequat massa quis enim. Done</p>
</section>

<!-- Orange panel + image -->
<section class="slide panel-slide">
  <div class="photo photo--night" style="left:198px;top:0;width:267px;height:262px" role="img" aria-label="Football players lined up at night on a grass field"></div>
  <div class="panel-side">
    <div class="abs panel-heading h-mont">Lorem ipsum dolor sit</div>
    <svg class="abs" style="left:20px;top:105px" width="16" height="16" viewBox="0 0 16 16"><path d="M1 1 H8 L15 8 L8 15 L1 8Z" fill="var(--white)"/><circle cx="5" cy="5" r="1.5" fill="var(--orange)"/></svg>
    <div class="abs panel-item" style="left:18px;top:128px"><h3>Your title here</h3><p>Lorem ipsum dolor sit amet, consectetuer adipiscing elit. Aenean commodo ligula eget dolor. Aenean massa. Cum sociis natoque</p></div>
    <svg class="abs" style="left:20px;top:178px" width="18" height="16" viewBox="0 0 18 16" fill="none" stroke="var(--white)" stroke-width="1.6"><path d="M1 2 H4 L6 10 H15 L17 4 H5"/><circle cx="7" cy="13.5" r="1.3"/><circle cx="14" cy="13.5" r="1.3"/></svg>
    <div class="abs panel-item" style="left:18px;top:200px"><h3>Your title here</h3><p>There are many variations of passages of lorem ipsum available, but the majority have suffered alteration in some form</p></div>
  </div>
  <div class="badge" style="left:166px;top:99px;width:64px;height:64px;border:4px solid var(--blue)"><div class="wordmark">Keenfield<br>Athletics</div></div>
</section>

<!-- Grid -->
<section class="slide grid-slide">
  <div class="abs grid-title h-mont">Lorem ipsum dolor sit ame</div>
  <div class="photo photo--action" style="left:2px;top:36px;width:230px;height:108px" role="img" aria-label="Football players in blue jerseys in a tackle"></div>
  <div class="grid-box" style="left:234px;top:36px;width:228px;height:108px;background:var(--blue)">
    <h3>Insert title here</h3>
    <div class="grid-row"><svg width="14" height="12" viewBox="0 0 14 12" fill="none" stroke="#fff" stroke-width="1.2"><rect x="1" y="2" width="9" height="9" rx="1"/><path d="M6 7 L12 1"/></svg><span>There are many variations of passages of lorem ipsum available, but the majority have suffered alteration in some form,</span></div>
    <div class="grid-row"><svg width="14" height="12" viewBox="0 0 14 12" fill="none" stroke="#fff" stroke-width="1.2"><rect x="1" y="2" width="9" height="9" rx="1"/><path d="M6 7 L12 1"/></svg><span>There are many variations of passages of lorem ipsum available, but the majority have suffered alteration in some form,</span></div>
  </div>
  <div class="grid-box grid-box--right" style="left:2px;top:151px;width:228px;height:111px;background:var(--orange)">
    <h3>Insert title here</h3>
    <div class="grid-row"><span style="padding-left:34px">There are many variations of passages of lorem ipsum available, but the majority have suffered alteration in some form,</span><svg width="14" height="12" viewBox="0 0 14 12" fill="none" stroke="#fff" stroke-width="1.2"><rect x="1" y="2" width="9" height="9" rx="1"/><path d="M6 7 L12 1"/></svg></div>
    <div class="grid-row"><span style="padding-left:34px">There are many variations of passages of lorem ipsum available, but the majority have suffered alteration in some form,</span><svg width="14" height="12" viewBox="0 0 14 12" fill="none" stroke="#fff" stroke-width="1.2"><rect x="1" y="2" width="9" height="9" rx="1"/><path d="M6 7 L12 1"/></svg></div>
  </div>
  <div class="photo photo--action" style="left:234px;top:151px;width:228px;height:111px;background:linear-gradient(120deg,#c8ccd4 0%,#2b47a8 45%,#7a4a2a 55%,#2a3f96 70%,#d8dbe2 100%)" role="img" aria-label="Quarterback in blue uniform holding the ball"></div>
</section>

<!-- Benefits -->
<section class="slide benefit-slide">
  <div class="photo photo--night" style="left:0;top:0;width:233px;height:262px" role="img" aria-label="Football team crouched in formation on a field at night"></div>
  <div class="abs benefit-title h-mont">Lorem ipsum dolor sit amet,</div>
  <div class="abs benefit-sub">Lorem ipsum dolor sit amet,</div>
  <div class="benefit" style="top:84px"><div class="tick" style="background:var(--orange)"><svg width="12" height="10" viewBox="0 0 12 10"><path d="M1 5 L4.5 8.5 L11 1.5" fill="none" stroke="#fff" stroke-width="2"/></svg></div><div><h4>Benefit Number One</h4><p>Lorem ipsum dolor sit amet, consectetuer<br>adipiscing elit. Aenean commodo ligula eget dolor.</p></div></div>
  <div class="benefit" style="top:126px"><div class="tick" style="background:var(--grey-box)"><svg width="12" height="10" viewBox="0 0 12 10"><path d="M1 5 L4.5 8.5 L11 1.5" fill="none" stroke="#fff" stroke-width="2"/></svg></div><div><h4>Benefit Number Two</h4><p>Lorem ipsum dolor sit amet, consectetuer<br>adipiscing elit. Aenean commodo ligula eget dolor.</p></div></div>
  <div class="benefit" style="top:168px"><div class="tick" style="background:var(--blue)"><svg width="12" height="10" viewBox="0 0 12 10"><path d="M1 5 L4.5 8.5 L11 1.5" fill="none" stroke="#fff" stroke-width="2"/></svg></div><div><h4>Benefit Number Three</h4><p>Lorem ipsum dolor sit amet, consectetuer<br>adipiscing elit. Aenean commodo ligula eget dolor.</p></div></div>
  <div class="benefit" style="top:210px"><div class="tick" style="background:var(--orange)"><svg width="12" height="10" viewBox="0 0 12 10"><path d="M1 5 L4.5 8.5 L11 1.5" fill="none" stroke="#fff" stroke-width="2"/></svg></div><div><h4>Benefit Number Four</h4><p>Lorem ipsum dolor sit amet, consectetuer<br>adipiscing elit. Aenean commodo ligula eget dolor.</p></div></div>
</section>

<!-- Stats -->
<section class="slide stats-slide">
  <div class="abs stats-title h-mont">Lorem ipsum dolor sit amet</div>
  <div class="abs stats-sub">Lorem ipsum dolor sit amet</div>
  <div class="photo photo--night" style="left:34px;top:62px;width:181px;height:131px" role="img" aria-label="Football linemen ready at the line of scrimmage at night"></div>
  <div class="stats-box">
    <p>Lorem Ipsum has two main statistical methodologies are<br>used in data analysis which summarizes data.</p>
    <p>Lorem Ipsum has two main statistical methodologies are<br>used in data analysis which summarizes data.</p>
    <p>Lorem Ipsum has two main statistical methodologies are<br>used in data analysis which summarizes data.</p>
    <p>Lorem Ipsum has two main statistical methodologies are<br>used in data analysis which summarizes data.</p>
  </div>
  <div class="abs stats-foot">Lorem ipsum dolor sit amet, consectetuer adipiscing elit. Aenean commodo ligula eget dolor. Aenean massa.</div>
  <div class="stripe-blue" style="left:44px;top:250px;width:420px;height:5px"></div>
  <div class="stripe-orange" style="left:44px;top:255px;width:420px;height:7px"></div>
  <div class="brand-tab" style="width:44px;height:32px"><div class="wordmark">Keenfield<br>Athletics</div></div>
</section>

</body>
</html>
```